Brantel Construction Core Values Wall Design

Core Values Wall Design for our Wall, I’m not exactly sure visually what we would want it to look like. Maybe some acrylic stand offs that could go on brick? If that’s a possibility. That’s where we have the most space in the office. But we could do other locations too.

These are our core values
• Safety
• Integrity
• Quality
• Client-Focused Solutions
• Continuous Improvement
• Positive Culture and Stewardship

Our vision/mission statement is Steady Craft Built.

```html
<!DOCTYPE html>
<html lang="en">
<head>
<meta charset="utf-8">
<title>Brantel Construction – Core Values</title>
<link rel="stylesheet" href="https://fonts.googleapis.com/css2?family=Barlow:wght@500&family=Montserrat:wght@700;800&display=swap">
<style>
  :root {
    --brand-blue: #1a5f9c;
    --brand-red: #ec2a30;
    --value-orange: #f7941d;
    --value-red: #ec2a30;
    --value-navy: #1a5f9c;
    --value-green: #8dc63f;
    --value-sky: #29a9e0;
    --value-teal: #14a79a;
    --label-ink: #14233f;
    --paper: #ffffff;
  }
  html, body {
    margin: 0;
    padding: 0;
    overflow: hidden;
    background: var(--paper);
  }
  .canvas {
    position: relative;
    width: 1200px;
    height: 720px;
    overflow: hidden;
    background: var(--paper);
  }
  .values-wall {
    position: absolute;
    inset: 0;
    width: 1200px;
    height: 720px;
  }
  .value-disc__art { fill: currentColor; }
  .value-disc__face { fill: var(--paper); }
  .gear-label {
    font-family: "Barlow", "Arial Narrow", sans-serif;
    font-weight: 500;
    fill: var(--label-ink);
    text-anchor: middle;
  }
  .gear-label--quality { fill: var(--value-navy); }

  .brand-name {
    position: absolute;
    left: 380px;
    top: 222px;
    width: 480px;
    text-align: center;
    font-family: "Montserrat", sans-serif;
    font-weight: 800;
    color: var(--brand-blue);
    margin: 0;
    line-height: 1;
  }
  .brand-name__main {
    display: block;
    font-size: 74px;
    letter-spacing: 1px;
  }
  .brand-name__sub {
    display: block;
    margin-top: 14px;
    font-size: 24px;
    letter-spacing: 14px;
    padding-left: 14px;
  }

  .tagline-band {
    position: absolute;
    top: 587px;
    height: 70px;
  }
  .tagline-band--left { left: 173px; width: 274px; background: var(--brand-blue); }
  .tagline-band--right { left: 787px; width: 297px; background: var(--brand-red); }

  .tagline {
    position: absolute;
    left: 447px;
    top: 587px;
    width: 340px;
    text-align: center;
    font-family: "Montserrat", sans-serif;
    font-weight: 700;
    margin: 0;
    line-height: 1;
  }
  .tagline__main {
    display: block;
    font-size: 37px;
    color: var(--brand-blue);
    letter-spacing: 1px;
  }
  .tagline__sub {
    display: block;
    margin-top: 9px;
    font-size: 20px;
    color: var(--brand-red);
    letter-spacing: 19px;
    padding-left: 19px;
  }
</style>
</head>
<body>
<main class="canvas">
  <svg class="values-wall" viewBox="0 0 1200 720" xmlns="http://www.w3.org/2000/svg" aria-label="Core values">
    <g class="value-disc value-disc--safety" style="color: var(--value-orange)">
      <circle class="value-disc__art" cx="355" cy="192" r="80" role="img" aria-label="Orange gear illustration"/>
      <circle class="value-disc__face" cx="355" cy="192" r="54"/>
      <text class="gear-label" x="355" y="200" font-size="23">SAFETY</text>
    </g>

    <g class="value-disc value-disc--integrity" style="color: var(--value-red)">
      <circle class="value-disc__art" cx="307" cy="341" r="63" role="img" aria-label="Red gear illustration"/>
      <circle class="value-disc__face" cx="307" cy="341" r="43"/>
      <text class="gear-label" x="308" y="347" font-size="15.5">INTEGRITY</text>
    </g>

    <g class="value-disc value-disc--quality" style="color: var(--value-navy)">
      <circle class="value-disc__art" cx="425" cy="411" r="58" role="img" aria-label="Navy gear illustration"/>
      <circle class="value-disc__face" cx="425" cy="411" r="39"/>
      <text class="gear-label gear-label--quality" x="428" y="418" font-size="16">QUALITY</text>
    </g>

    <g class="value-disc value-disc--client" style="color: var(--value-green)">
      <circle class="value-disc__art" cx="813" cy="143" r="80" role="img" aria-label="Green gear illustration"/>
      <circle class="value-disc__face" cx="813" cy="143" r="54"/>
      <text class="gear-label" x="813" y="125" font-size="16">CLIENT</text>
      <text class="gear-label" x="813" y="144" font-size="16">FOCUSED</text>
      <text class="gear-label" x="815" y="163" font-size="16">SOLUTIONS</text>
    </g>

    <g class="value-disc value-disc--improvement" style="color: var(--value-sky)">
      <circle class="value-disc__art" cx="921" cy="303" r="92" role="img" aria-label="Sky blue gear illustration"/>
      <circle class="value-disc__face" cx="921" cy="303" r="61"/>
      <text class="gear-label" x="921" y="295" font-size="16">CONTINUOUS</text>
      <text class="gear-label" x="922" y="314" font-size="16">IMPROVEMENT</text>
    </g>

    <g class="value-disc value-disc--culture" style="color: var(--value-teal)">
      <circle class="value-disc__art" cx="779" cy="425" r="80" role="img" aria-label="Teal gear illustration"/>
      <circle class="value-disc__face" cx="779" cy="425" r="54"/>
      <text class="gear-label" x="780" y="404" font-size="14">POSITIVE</text>
      <text class="gear-label" x="780" y="420" font-size="14">CULTURE</text>
      <text class="gear-label" x="780" y="436" font-size="14">AND</text>
      <text class="gear-label" x="781" y="452" font-size="14">STEWARDSHIP</text>
    </g>
  </svg>

  <h1 class="brand-name">
    <span class="brand-name__main">BRANTEL</span>
    <span class="brand-name__sub">CONSTRUCTION</span>
  </h1>

  <div class="tagline-band tagline-band--left"></div>
  <div class="tagline-band tagline-band--right"></div>
  <p class="tagline">
    <span class="tagline__main">STEADY CRAFT</span>
    <span class="tagline__sub">BUILT</span>
  </p>
</main>
</body>
</html>
```